Trevolar bonds (Surety bond broker)

We are a broker of surety bonds, we need a presentation and a flyer with fresh design. Our core values are reliable, on time and customized service. We want to transmit to our clients, they can leave on us the process of underwriting and issuing a surety bond, so they can focus on their business with no distractions.

Font styles to use
Sans Serif
Other font styles liked:
• view logos

Requirements
Must have
• Visually attractive.
Main Message: Fast service issuing and underwriting surety bonds, reliable, nos surprises, we are always one step ahead, customized and personalized bonding solutions.
Nice to have
• Have short version for the flyer, and extended version for the presentation.
Should not have
• We already have a logo (attached), maintain colors

```html
<!DOCTYPE html>
<html lang="es">
<head>
<meta charset="utf-8">
<title>Trevolar Bonds – Índice y ¿Quiénes somos?</title>
<link href="https://fonts.googleapis.com/css2?family=Aleo:wght@400;500;600&display=swap" rel="stylesheet">
<style>
  :root {
    --page-bg: #efebe5;
    --charcoal: #58585a;
    --charcoal-dark: #3f3f41;
    --leaf: #7ab861;
    --leaf-deep: #5e9f48;
    --leaf-pale: #dcebc6;
    --paper: #ffffff;
    --ink: #3a3a3a;
    --muted: #9a9a9a;
  }
  * { margin: 0; padding: 0; box-sizing: border-box; }
  html, body { width: 1200px; height: 900px; overflow: hidden; }
  body {
    background: var(--page-bg);
    font-family: "Aleo", Georgia, serif;
    color: var(--ink);
  }
  .spread {
    position: absolute;
    left: 40px; top: 230px;
    width: 1120px; height: 440px;
    background: var(--paper);
    box-shadow: 0 10px 30px rgba(0,0,0,.18);
    overflow: hidden;
  }
  .spread-shapes { position: absolute; inset: 0; }
  .index-title {
    position: absolute; left: 20px; top: 200px;
    font-size: 36px; font-weight: 500; color: var(--leaf);
  }
  .index-list {
    position: absolute; left: 222px; top: 104px;
    list-style: none; font-size: 15px; color: var(--ink);
  }
  .index-list li { height: 38px; }
  .index-list .num { color: var(--muted); margin-right: 6px; }
  .index-list .sep { color: var(--muted); margin-right: 8px; }
  .about-title {
    position: absolute; left: 590px; top: 170px; width: 220px;
    text-align: center; font-size: 34px; line-height: 1.05;
    font-weight: 500; color: var(--paper);
  }
  .about-text {
    position: absolute; left: 890px; top: 62px; width: 208px;
    font-size: 10.5px; line-height: 1.35; text-align: justify; color: var(--ink);
  }
  .about-text p { margin-bottom: 12px; }
  .brand {
    position: absolute; display: flex; align-items: center; gap: 6px;
    font-size: 17px; font-weight: 500; color: var(--leaf-deep);
    letter-spacing: .5px;
  }
  .brand-square { width: 10px; height: 10px; background: var(--charcoal); }
  .brand--index { left: 420px; top: 392px; }
  .brand--about { left: 985px; top: 392px; }
</style>
</head>
<body>
  <section class="spread">
    <svg class="spread-shapes" width="1120" height="440" viewBox="0 0 1120 440" aria-hidden="true">
      <defs>
        <linearGradient id="wash" x1="0" y1="0" x2="0.3" y2="1">
          <stop offset="0" stop-color="#c9e0a8"/>
          <stop offset="0.55" stop-color="#eaf3dc"/>
          <stop offset="1" stop-color="#ffffff"/>
        </linearGradient>
        <linearGradient id="leafPanel" x1="0" y1="0" x2="0" y2="1">
          <stop offset="0" stop-color="#8cc46f"/>
          <stop offset="1" stop-color="#74b25a"/>
        </linearGradient>
      </defs>
      <rect class="wash" x="0" y="0" width="1120" height="440" fill="url(#wash)"/>
      <line class="fold" x1="560" y1="0" x2="560" y2="440" stroke="#000" stroke-opacity=".06"/>

      <path class="index-band" d="M0 0 H160 C140 150 130 300 100 440 H0Z" fill="var(--charcoal)"/>
      <path class="index-stripe-dark" d="M178 0 H200 C180 180 170 320 130 440 H118 C150 300 160 160 178 0Z" fill="var(--charcoal-dark)"/>
      <path class="index-swoosh" d="M214 40 C202 200 182 340 142 440 H130 C170 340 192 200 214 40Z" fill="var(--leaf)"/>

      <path class="about-panel" d="M560 0 H830 C810 160 790 320 750 440 H560Z" fill="url(#leafPanel)"/>
      <path class="about-stripe-dark" d="M838 0 H866 C846 170 820 320 776 440 H758 C798 320 818 160 838 0Z" fill="var(--charcoal-dark)"/>
      <path class="about-swoosh" d="M872 60 C857 220 832 350 792 440 H781 C824 340 849 220 872 60Z" fill="var(--leaf)"/>
    </svg>

    <h2 class="index-title">Índice</h2>
    <ol class="index-list">
      <li><span class="num">1</span><span class="sep">|</span>¿Quiénes somos?</li>
      <li><span class="num">2</span><span class="sep">|</span>Oferta de Valor</li>
      <li><span class="num">3</span><span class="sep">|</span>Nuestros Servicios</li>
      <li><span class="num">4</span><span class="sep">|</span>Productos</li>
      <li><span class="num">5</span><span class="sep">|</span>Ciclo de administración de Fianzas</li>
      <li><span class="num">6</span><span class="sep">|</span>Nuestros socios de negocio</li>
      <li><span class="num">7</span><span class="sep">|</span>Contacto</li>
    </ol>
    <div class="brand brand--index"><span class="brand-square"></span>TREVOLAR</div>

    <h2 class="about-title">¿Quiénes somos?</h2>
    <div class="about-text">
      <p>Trevolar Bonds, somos un grupo de jóvenes emprendedores, con amplia experiencia en el sector afianzador.</p>
      <p>Estamos convencidos de que nuestro principal diferenciador es la pasión por el servicio.</p>
      <p>Nuestra prioridad es el éxito de cada uno de nuestros clientes, nos aseguramos de que el “trámite” de fianzas deje de ser un “trámite” y se convierta en la llave del éxito para cada uno de nuestros fiados y beneficiarios.</p>
      <p>Buscamos siempre tener relaciones estrechas y de largo plazo con todos nuestros “stakeholders”. Por lo que nos rodeamos del mejor talento en el sector para garantizar a nuestros clientes un servicio personalizado, en tiempo y confiable.</p>
    </div>
    <div class="brand brand--about"><span class="brand-square"></span>TREVOLAR</div>
  </section>
</body>
</html>
```